Book Cover for Notes on the Quiet River's Far Lamps

I need a book cover for a 6 x 9 paperback titled Notes on the Quiet River's Far Lamps Gathered by Sailors and Weavers Resting in the Valley beyond the Northern Valley. It has to do with consciousness, the mind, incarnation onto Earth, leaving Earth, and the life in the life after this life. I have an idea I'm providing with this description, but I am open to anything that would be striking and stimulating, whether with a book or not. I am the author, T. Warren Blakely. I've added another background idea to see if anyone can do something with it and I've increased the budget.

```html
<!DOCTYPE html>
<html lang="en">
<head>
<meta charset="utf-8">
<title>Notes on the Quiet River's Far Lamps — T. Warren Blakely</title>
<link rel="stylesheet" href="https://fonts.googleapis.com/css2?family=Cormorant+Garamond:wght@600&family=Prata&display=swap">
<style>
  :root {
    --cover-black: #070405;
    --deep-brown: #2a1a0e;
    --amber-glow: #9a7038;
    --light-core: #f6e2b0;
    --title-gold: #d9b771;
    --subtitle-white: #fbf7f0;
  }
  html, body {
    margin: 0;
    padding: 0;
    width: 800px;
    height: 1200px;
    overflow: hidden;
    background: var(--cover-black);
  }
  .cover {
    position: relative;
    width: 800px;
    height: 1200px;
    overflow: hidden;
    background:
      radial-gradient(ellipse 330px 420px at 400px 700px,
        var(--amber-glow) 0%,
        #6b4a22 30%,
        var(--deep-brown) 58%,
        var(--cover-black) 85%),
      var(--cover-black);
  }
  .cover__title {
    position: absolute;
    top: 82px;
    left: 0;
    width: 800px;
    margin: 0;
    text-align: center;
    font-family: "Cormorant Garamond", serif;
    font-weight: 600;
    font-size: 146px;
    line-height: 1;
    letter-spacing: 2px;
    color: var(--title-gold);
  }
  .cover__subtitle {
    position: absolute;
    top: 236px;
    left: 60px;
    width: 680px;
    margin: 0;
    text-align: center;
    font-family: "Prata", serif;
    font-weight: 400;
    font-size: 29px;
    line-height: 53px;
    color: var(--subtitle-white);
  }
  .cover__book-art {
    position: absolute;
    left: 62px;
    top: 600px;
    width: 656px;
    height: 290px;
    border-radius: 40% 40% 8px 8px / 60% 60% 8px 8px;
    background: radial-gradient(ellipse at 50% 40%,
      var(--light-core) 0%,
      #d9ac68 35%,
      #a8743c 65%,
      rgba(90, 58, 28, 0.2) 100%);
  }
  .cover__author {
    position: absolute;
    top: 1040px;
    left: 0;
    width: 800px;
    margin: 0;
    text-align: center;
    font-family: "Cormorant Garamond", serif;
    font-weight: 600;
    font-size: 66px;
    line-height: 1;
    color: var(--title-gold);
  }
</style>
</head>
<body>
  <main class="cover">
    <h1 class="cover__title">NOTES</h1>
    <p class="cover__subtitle">on the Quiet River's Far Lamps Gathered by Sailors and Weavers Resting in the Valley beyond the Northern Valley</p>
    <div class="cover__book-art" role="img" aria-label="An old open book with fanning pages, glowing with warm golden light from its centre"></div>
    <p class="cover__author">T. Warren Blakely</p>
  </main>
</body>
</html>
```